Design Website for Data Entry

Design a single webpage website with three tabs, or section for. See the attached PDF for info. This webpage is a data entry dadshboard.

Target Market(s)

N/A

Number of Pages Required

3 page

Colors

Designer to choose colors to be used in the design.

```html
<!DOCTYPE html>
<html lang="en">
<head>
<meta charset="utf-8">
<title>Kestrel Data Entry Dashboard</title>
<link href="https://fonts.googleapis.com/css2?family=Open+Sans:wght@400;600;700&display=swap" rel="stylesheet">
<style>
:root{
  --page:#d5d5d5;
  --navy:#13262f;
  --orange:#f47b20;
  --orange-deep:#e86d27;
  --panel:#eef0f3;
  --card:#f3f5f8;
  --ink:#2b2b2b;
  --muted:#6d6d6d;
  --white:#ffffff;
  --line:#c9c9c9;
  --ok:#2e9b3a;
  --bad:#d6262f;
}
*{box-sizing:border-box;margin:0;padding:0}
html,body{width:1200px;height:2594px;overflow:hidden}
body{background:var(--page);font-family:"Open Sans",Arial,sans-serif;position:relative;color:var(--ink)}
.screen{position:absolute;left:90px;width:1003px;height:757px;background:var(--white);box-shadow:0 2px 6px rgba(0,0,0,.12)}
.screen--files{top:83px}
.screen--videos{top:916px}
.screen--messages{top:1750px}

/* sidebar */
.sidebar{position:absolute;left:0;top:0;width:264px;height:100%;background:var(--navy);color:var(--white)}
.sidebar__head{position:absolute;top:12px;left:24px;right:16px;height:24px;display:flex;align-items:center}
.sidebar__title{font-weight:700;font-size:17px;margin-left:14px;letter-spacing:.3px}
.sidebar__gear{margin-left:auto}
.profile__avatar{position:absolute;left:90px;top:70px;width:84px;height:84px;border-radius:50%;border:3px solid #e9e4de;background:linear-gradient(160deg,#d9d2c8,#a79a8c 60%,#4b5058)}
.profile__status{position:absolute;left:158px;top:138px;width:13px;height:13px;border-radius:50%;background:#2fbf45;border:2px solid var(--navy)}
.profile__name{position:absolute;top:152px;left:0;width:100%;text-align:center;font-size:17px;font-weight:600}
.profile__mail{position:absolute;top:180px;left:0;width:100%;text-align:center;font-size:11px;color:#d6dde1}
.create-btn{position:absolute;left:47px;top:216px;width:171px;height:42px;border-radius:12px;background:var(--orange);font-size:11.5px;font-weight:700;display:flex;align-items:center;justify-content:center;text-transform:uppercase}
.nav{position:absolute;top:299px;left:0;width:100%;list-style:none}
.nav__item{position:relative;height:38.7px;display:flex;align-items:center;padding-left:60px;font-size:12.5px;font-weight:700;text-transform:uppercase}
.nav__icon{position:absolute;left:28px;top:13px}
.nav__item--active{color:var(--orange)}
.nav__marker{position:absolute;left:-9px;top:8px;width:22px;height:22px;border-radius:50%;background:var(--orange)}
.nav__badge{position:absolute;left:194px;top:8px;width:50px;height:23px;border-radius:12px;background:var(--orange);color:var(--white);font-size:12px;font-weight:600;display:flex;align-items:center;justify-content:center}
.nav__plus{position:absolute;left:230px;font-size:14px;font-weight:700;color:var(--white)}

/* main */
.topbar{position:absolute;left:264px;top:0;right:0;height:90px}
.brand{position:absolute;left:22px;top:24px;display:flex;align-items:center;gap:8px}
.brand__mark{width:30px;height:30px;border:3px solid var(--navy);border-radius:7px}
.brand__name{font-size:25px;font-weight:700;color:var(--orange);letter-spacing:.5px}
.search-icon{position:absolute;left:559px;top:41px}
.topbar__divider{position:absolute;left:590px;top:30px;width:1px;height:34px;background:#ddd}
.adv-btn{position:absolute;left:609px;top:33px;width:121px;height:33px;border-radius:10px;background:var(--orange);color:var(--white);font-size:10px;font-weight:600;display:flex;align-items:center;justify-content:center;text-transform:uppercase}
.section-band{position:absolute;left:275px;top:90px;width:719px;height:64px;background:linear-gradient(90deg,var(--orange),var(--orange-deep));color:var(--white);font-size:17px;font-weight:700;text-transform:uppercase;display:flex;align-items:center;justify-content:center;letter-spacing:.4px}
.panel{position:absolute;left:289px;top:171px;width:705px;height:546px;background:var(--panel)}
.scrollbar{position:absolute;right:0;top:0;width:22px;height:100%;background:#e7e9ec;border-left:1px solid #dcdfe3}
.scrollbar span{position:absolute;left:7px;font-size:9px;color:#888}
.list{position:absolute;left:23px;top:19px;width:635px;display:flex;flex-direction:column;gap:22px}
.item{height:104px;background:var(--card);border-left:3px solid var(--orange);box-shadow:0 2px 4px rgba(0,0,0,.12);display:flex;padding:16px 0 0 31px}
.item__thumb{width:87px;height:72px;border-radius:6px;flex:none;box-shadow:0 1px 3px rgba(0,0,0,.2)}
.thumb--logo-a{background:linear-gradient(135deg,#ffffff,#e4e7ea)}
.thumb--logo-b{background:radial-gradient(circle,#f3a24a 0,#3a73c9 45%,#ffffff 70%)}
.thumb--logo-c{background:radial-gradient(circle,#2a5db0 0,#6a95d8 35%,#ffffff 62%)}
.thumb--logo-d{background:linear-gradient(135deg,#ffffff,#d8d8d8)}
.thumb--video-a{background:linear-gradient(135deg,#0f2c55,#2d6eb0 55%,#0b1f3d)}
.thumb--video-b{background:linear-gradient(135deg,#5c3a2a,#2f4a6c 50%,#b8cbe0)}
.thumb--video-c{background:linear-gradient(135deg,#112a4d,#4f86c4 55%,#1b355c)}
.thumb--video-d{background:linear-gradient(135deg,#3a4f75,#8a6a5a 50%,#cbd7e6)}
.item__body{margin-left:27px;width:470px}
.item__title{font-size:13.5px;font-weight:600;color:#333;line-height:1.1}
.item__text{font-size:9px;color:var(--muted);line-height:1.5;margin-top:5px}
.item__actions{display:flex;align-items:center;gap:14px;margin-top:6px}
.btn-edit{width:38px;height:21px;border-radius:5px;background:var(--orange);color:var(--white);font-size:9.5px;display:flex;align-items:center;justify-content:center}
.btn-delete{width:55px;height:21px;border-radius:5px;border:1px solid var(--orange);color:var(--orange);font-size:9.5px;display:flex;align-items:center;justify-content:center}
.status{font-size:9.5px;display:flex;align-items:center;gap:3px}
.status--ok{color:var(--ok)}
.status--bad{color:var(--bad)}
.add-btn{position:absolute;left:332px;top:509px;width:42px;height:23px;background:#e1e4e8;border:1px solid #d2d6db;display:flex;align-items:center;justify-content:center;font-size:17px;font-weight:700;color:#777}
.footer{position:absolute;left:264px;right:0;top:733px;text-align:center;font-size:10px;color:#444;padding-right:240px}
.forms{position:absolute;left:23px;top:2px;width:635px;display:flex;flex-direction:column;gap:12px}
.field{background:var(--card);border-left:3px solid var(--orange);box-shadow:0 2px 4px rgba(0,0,0,.12);padding:8px 0 0 31px}
.field__label{font-size:13px;font-weight:600;color:#333}
.field__input{width:579px;margin-top:8px;border:1px solid var(--line);background:#f7f7f7}
</style>
</head>
<body>

<!-- FILE UPLOAD -->
<section class="screen screen--files">
  <aside class="sidebar">
    <div class="sidebar__head">
      <svg width="16" height="14" viewBox="0 0 16 14"><rect y="0" width="16" height="2.4" fill="#fff"/><rect y="5.8" width="16" height="2.4" fill="#fff"/><rect y="11.6" width="16" height="2.4" fill="#fff"/></svg>
      <span class="sidebar__title">MENU</span>
      <svg class="sidebar__gear" width="16" height="16" viewBox="0 0 16 16"><circle cx="8" cy="8" r="5.5" fill="none" stroke="#fff" stroke-width="3" stroke-dasharray="3 1.3"/><circle cx="8" cy="8" r="2" fill="#fff"/></svg>
    </div>
    <div class="profile__avatar" role="img" aria-label="Profile photo of the signed-in user"></div>
    <div class="profile__status"></div>
    <div class="profile__name">Daniel Reyes</div>
    <div class="profile__mail">UserID@mailbox.test</div>
    <div class="create-btn">+ Create a document</div>
    <ul class="nav">
      <li class="nav__item nav__item--active"><span class="nav__marker"></span><svg class="nav__icon" width="12" height="12" viewBox="0 0 12 12"><path d="M1 10a5 5 0 0 1 10 0z" fill="#f47b20"/></svg>Dashboard<span class="nav__badge">57</span></li>
      <li class="nav__item"><svg class="nav__icon" width="12" height="12" viewBox="0 0 12 12"><rect x="0" y="3" width="12" height="8" rx="1" fill="#fff"/><rect x="4" y="1" width="4" height="2" fill="#fff"/></svg>Main<span class="nav__plus">+</span></li>
      <li class="nav__item"><svg class="nav__icon" width="12" height="12" viewBox="0 0 12 12"><rect x="0.5" y="1.5" width="11" height="10" fill="none" stroke="#fff"/><rect x="0.5" y="1.5" width="11" height="3" fill="#fff"/></svg>Kestrel</li>
      <li class="nav__item"><svg class="nav__icon" width="12" height="12" viewBox="0 0 12 12"><polyline points="0,11 4,6 7,8 12,2" fill="none" stroke="#fff" stroke-width="1.5"/></svg>Reports</li>
      <li class="nav__item"><svg class="nav__icon" width="13" height="12" viewBox="0 0 13 12"><circle cx="4" cy="4" r="2.5" fill="#fff"/><circle cx="9" cy="4" r="2.5" fill="#fff"/><rect x="0" y="7" width="13" height="4" rx="2" fill="#fff"/></svg>Self service</li>
      <li class="nav__item"><svg class="nav__icon" width="11" height="12" viewBox="0 0 11 12"><path d="M1 .5h6l3 3V11.5H1z" fill="none" stroke="#fff"/></svg>Documents</li>
      <li class="nav__item"><svg class="nav__icon" width="12" height="12" viewBox="0 0 12 12"><circle cx="6" cy="6" r="4" fill="none" stroke="#fff" stroke-width="2.5" stroke-dasharray="2 1"/></svg>Settings<span class="nav__plus">+</span></li>
      <li class="nav__item"><svg class="nav__icon" width="12" height="12" viewBox="0 0 12 12"><text x="3" y="11" font-size="12" font-weight="700" fill="#fff" font-family="Open Sans, sans-serif">?</text></svg>Help<span class="nav__plus">+</span></li>
    </ul>
  </aside>
  <header class="topbar">
    <div class="brand"><span class="brand__mark"></span><span class="brand__name">KESTREL</span></div>
    <svg class="search-icon" width="12" height="12" viewBox="0 0 12 12"><circle cx="5" cy="5" r="3.8" fill="none" stroke="#555" stroke-width="1.6"/><line x1="8" y1="8" x2="11.5" y2="11.5" stroke="#555" stroke-width="1.8"/></svg>
    <span class="topbar__divider"></span>
    <div class="adv-btn">Advanced search</div>
  </header>
  <div class="section-band">File upload</div>
  <div class="panel">
    <div class="scrollbar"><span style="top:6px">&#9650;</span><span style="bottom:6px">&#9660;</span></div>
    <div class="list">
      <article class="item"><div class="item__thumb thumb--logo-a" role="img" aria-label="Uploaded file thumbnail: company logo"></div><div class="item__body"><h3 class="item__title">Lorem ipsum dolor</h3><p class="item__text">Sed ut perspiciatis unde omnis iste natus error sit voluptatem accusantium doloremque laudantium, totam rem aperiam, eaque ipsa quae ab illo inventore veritatis et quasi architecto beatae.</p><div class="item__actions"><span class="btn-edit">Edit</span><span class="btn-delete">Delete</span><span class="status status--ok">&#10004; Status</span></div></div></article>
      <article class="item"><div class="item__thumb thumb--logo-b" role="img" aria-label="Uploaded file thumbnail: company logo"></div><div class="item__body"><h3 class="item__title">Lorem ipsum dolor</h3><p class="item__text">Sed ut perspiciatis unde omnis iste natus error sit voluptatem accusantium doloremque laudantium, totam rem aperiam, eaque ipsa quae ab illo inventore veritatis et quasi architecto beatae.</p><div class="item__actions"><span class="btn-edit">Edit</span><span class="btn-delete">Delete</span><span class="status status--bad">&#10006; Status</span></div></div></article>
      <article class="item"><div class="item__thumb thumb--logo-c" role="img" aria-label="Uploaded file thumbnail: company logo"></div><div class="item__body"><h3 class="item__title">Lorem ipsum dolor</h3><p class="item__text">Sed ut perspiciatis unde omnis iste natus error sit voluptatem accusantium doloremque laudantium, totam rem aperiam, eaque ipsa quae ab illo inventore veritatis et quasi architecto beatae.</p><div class="item__actions"><span class="btn-edit">Edit</span><span class="btn-delete">Delete</span><span class="status status--ok">&#10004; Status</span></div></div></article>
      <article class="item"><div class="item__thumb thumb--logo-d" role="img" aria-label="Uploaded file thumbnail: company logo"></div><div class="item__body"><h3 class="item__title">Lorem ipsum dolor</h3><p class="item__text">Sed ut perspiciatis unde omnis iste natus error sit voluptatem accusantium doloremque laudantium, totam rem aperiam, eaque ipsa quae ab illo inventore veritatis et quasi architecto beatae.</p><div class="item__actions"><span class="btn-edit">Edit</span><span class="btn-delete">Delete</span><span class="status status--bad">&#10006; Status</span></div></div></article>
    </div>
    <div class="add-btn">+</div>
  </div>
  <footer class="footer">Copyrights© 2018 . All Rights Reserved.</footer>
</section>

<!-- VIDEO UPLOAD -->
<section class="screen screen--videos">
  <aside class="sidebar">
    <div class="sidebar__head">
      <svg width="16" height="14" viewBox="0 0 16 14"><rect y="0" width="16" height="2.4" fill="#fff"/><rect y="5.8" width="16" height="2.4" fill="#fff"/><rect y="11.6" width="16" height="2.4" fill="#fff"/></svg>
      <span class="sidebar__title">MENU</span>
      <svg class="sidebar__gear" width="16" height="16" viewBox="0 0 16 16"><circle cx="8" cy="8" r="5.5" fill="none" stroke="#fff" stroke-width="3" stroke-dasharray="3 1.3"/><circle cx="8" cy="8" r="2" fill="#fff"/></svg>
    </div>
    <div class="profile__avatar" role="img" aria-label="Profile photo of the signed-in user"></div>
    <div class="profile__status"></div>
    <div class="profile__name">Daniel Reyes</div>
    <div class="profile__mail">UserID@mailbox.test</div>
    <div class="create-btn">+ Create a document</div>
    <ul class="nav">
      <li class="nav__item nav__item--active"><span class="nav__marker"></span><svg class="nav__icon" width="12" height="12" viewBox="0 0 12 12"><path d="M1 10a5 5 0 0 1 10 0z" fill="#f47b20"/></svg>Dashboard<span class="nav__badge">57</span></li>
      <li class="nav__item"><svg class="nav__icon" width="12" height="12" viewBox="0 0 12 12"><rect x="0" y="3" width="12" height="8" rx="1" fill="#fff"/><rect x="4" y="1" width="4" height="2" fill="#fff"/></svg>Main<span class="nav__plus">+</span></li>
      <li class="nav__item"><svg class="nav__icon" width="12" height="12" viewBox="0 0 12 12"><rect x="0.5" y="1.5" width="11" height="10" fill="none" stroke="#fff"/><rect x="0.5" y="1.5" width="11" height="3" fill="#fff"/></svg>Kestrel</li>
      <li class="nav__item"><svg class="nav__icon" width="12" height="12" viewBox="0 0 12 12"><polyline points="0,11 4,6 7,8 12,2" fill="none" stroke="#fff" stroke-width="1.5"/></svg>Reports</li>
      <li class="nav__item"><svg class="nav__icon" width="13" height="12" viewBox="0 0 13 12"><circle cx="4" cy="4" r="2.5" fill="#fff"/><circle cx="9" cy="4" r="2.5" fill="#fff"/><rect x="0" y="7" width="13" height="4" rx="2" fill="#fff"/></svg>Self service</li>
      <li class="nav__item"><svg class="nav__icon" width="11" height="12" viewBox="0 0 11 12"><path d="M1 .5h6l3 3V11.5H1z" fill="none" stroke="#fff"/></svg>Documents</li>
      <li class="nav__item"><svg class="nav__icon" width="12" height="12" viewBox="0 0 12 12"><circle cx="6" cy="6" r="4" fill="none" stroke="#fff" stroke-width="2.5" stroke-dasharray="2 1"/></svg>Settings<span class="nav__plus">+</span></li>
      <li class="nav__item"><svg class="nav__icon" width="12" height="12" viewBox="0 0 12 12"><text x="3" y="11" font-size="12" font-weight="700" fill="#fff" font-family="Open Sans, sans-serif">?</text></svg>Help<span class="nav__plus">+</span></li>
    </ul>
  </aside>
  <header class="topbar">
    <div class="brand"><span class="brand__mark"></span><span class="brand__name">KESTREL</span></div>
    <svg class="search-icon" width="12" height="12" viewBox="0 0 12 12"><circle cx="5" cy="5" r="3.8" fill="none" stroke="#555" stroke-width="1.6"/><line x1="8" y1="8" x2="11.5" y2="11.5" stroke="#555" stroke-width="1.8"/></svg>
    <span class="topbar__divider"></span>
    <div class="adv-btn">Advanced search</div>
  </header>
  <div class="section-band">Video upload</div>
  <div class="panel">
    <div class="scrollbar"><span style="top:6px">&#9650;</span><span style="bottom:6px">&#9660;</span></div>
    <div class="list">
      <article class="item"><div class="item__thumb thumb--video-a" role="img" aria-label="Video thumbnail: blue technology still"></div><div class="item__body"><h3 class="item__title">Lorem ipsum dolor</h3><p class="item__text">Sed ut perspiciatis unde omnis iste natus error sit voluptatem accusantium doloremque laudantium, totam rem aperiam, eaque ipsa quae ab illo inventore veritatis et quasi architecto beatae.</p><div class="item__actions"><span class="btn-edit">Edit</span><span class="btn-delete">Delete</span></div></div></article>
      <article class="item"><div class="item__thumb thumb--video-b" role="img" aria-label="Video thumbnail: people working at computers"></div><div class="item__body"><h3 class="item__title">Lorem ipsum dolor</h3><p class="item__text">Sed ut perspiciatis unde omnis iste natus error sit voluptatem accusantium doloremque laudantium, totam rem aperiam, eaque ipsa quae ab illo inventore veritatis et quasi architecto beatae.</p><div class="item__actions"><span class="btn-edit">Edit</span><span class="btn-delete">Delete</span></div></div></article>
      <article class="item"><div class="item__thumb thumb--video-c" role="img" aria-label="Video thumbnail: digital network still"></div><div class="item__body"><h3 class="item__title">Lorem ipsum dolor</h3><p class="item__text">Sed ut perspiciatis unde omnis iste natus error sit voluptatem accusantium doloremque laudantium, totam rem aperiam, eaque ipsa quae ab illo inventore veritatis et quasi architecto beatae.</p><div class="item__actions"><span class="btn-edit">Edit</span><span class="btn-delete">Delete</span></div></div></article>
      <article class="item"><div class="item__thumb thumb--video-d" role="img" aria-label="Video thumbnail: office meeting still"></div><div class="item__body"><h3 class="item__title">Lorem ipsum dolor</h3><p class="item__text">Sed ut perspiciatis unde omnis iste natus error sit voluptatem accusantium doloremque laudantium, totam rem aperiam, eaque ipsa quae ab illo inventore veritatis et quasi architecto beatae.</p><div class="item__actions"><span class="btn-edit">Edit</span><span class="btn-delete">Delete</span></div></div></article>
    </div>
    <div class="add-btn">+</div>
  </div>
  <footer class="footer">Copyrights© 2018 . All Rights Reserved.</footer>
</section>

<!-- MESSAGES -->
<section class="screen screen--messages">
  <aside class="sidebar">
    <div class="sidebar__head">
      <svg width="16" height="14" viewBox="0 0 16 14"><rect y="0" width="16" height="2.4" fill="#fff"/><rect y="5.8" width="16" height="2.4" fill="#fff"/><rect y="11.6" width="16" height="2.4" fill="#fff"/></svg>
      <span class="sidebar__title">MENU</span>
      <svg class="sidebar__gear" width="16" height="16" viewBox="0 0 16 16"><circle cx="8" cy="8" r="5.5" fill="none" stroke="#fff" stroke-width="3" stroke-dasharray="3 1.3"/><circle cx="8" cy="8" r="2" fill="#fff"/></svg>
    </div>
    <div class="profile__avatar" role="img" aria-label="Profile photo of the signed-in user"></div>
    <div class="profile__status"></div>
    <div class="profile__name">Daniel Reyes</div>
    <div class="profile__mail">UserID@mailbox.test</div>
    <div class="create-btn">+ Create a document</div>
    <ul class="nav">
      <li class="nav__item nav__item--active"><span class="nav__marker"></span><svg class="nav__icon" width="12" height="12" viewBox="0 0 12 12"><path d="M1 10a5 5 0 0 1 10 0z" fill="#f47b20"/></svg>Dashboard<span class="nav__badge">57</span></li>
      <li class="nav__item"><svg class="nav__icon" width="12" height="12" viewBox="0 0 12 12"><rect x="0" y="3" width="12" height="8" rx="1" fill="#fff"/><rect x="4" y="1" width="4" height="2" fill="#fff"/></svg>Main<span class="nav__plus">+</span></li>
      <li class="nav__item"><svg class="nav__icon" width="12" height="12" viewBox="0 0 12 12"><rect x="0.5" y="1.5" width="11" height="10" fill="none" stroke="#fff"/><rect x="0.5" y="1.5" width="11" height="3" fill="#fff"/></svg>Kestrel</li>
      <li class="nav__item"><svg class="nav__icon" width="12" height="12" viewBox="0 0 12 12"><polyline points="0,11 4,6 7,8 12,2" fill="none" stroke="#fff" stroke-width="1.5"/></svg>Reports</li>
      <li class="nav__item"><svg class="nav__icon" width="13" height="12" viewBox="0 0 13 12"><circle cx="4" cy="4" r="2.5" fill="#fff"/><circle cx="9" cy="4" r="2.5" fill="#fff"/><rect x="0" y="7" width="13" height="4" rx="2" fill="#fff"/></svg>Self service</li>
      <li class="nav__item"><svg class="nav__icon" width="11" height="12" viewBox="0 0 11 12"><path d="M1 .5h6l3 3V11.5H1z" fill="none" stroke="#fff"/></svg>Documents</li>
      <li class="nav__item"><svg class="nav__icon" width="12" height="12" viewBox="0 0 12 12"><circle cx="6" cy="6" r="4" fill="none" stroke="#fff" stroke-width="2.5" stroke-dasharray="2 1"/></svg>Settings<span class="nav__plus">+</span></li>
      <li class="nav__item"><svg class="nav__icon" width="12" height="12" viewBox="0 0 12 12"><text x="3" y="11" font-size="12" font-weight="700" fill="#fff" font-family="Open Sans, sans-serif">?</text></svg>Help<span class="nav__plus">+</span></li>
    </ul>
  </aside>
  <header class="topbar">
    <div class="brand"><span class="brand__mark"></span><span class="brand__name">KESTREL</span></div>
    <svg class="search-icon" width="12" height="12" viewBox="0 0 12 12"><circle cx="5" cy="5" r="3.8" fill="none" stroke="#555" stroke-width="1.6"/><line x1="8" y1="8" x2="11.5" y2="11.5" stroke="#555" stroke-width="1.8"/></svg>
    <span class="topbar__divider"></span>
    <div class="adv-btn">Advanced search</div>
  </header>
  <div class="section-band">Messages</div>
  <div class="panel">
    <div class="scrollbar"><span style="top:6px">&#9650;</span><span style="bottom:6px">&#9660;</span></div>
    <div class="forms">
      <div class="field" style="height:100px"><div class="field__label">Welcome message</div><div class="field__input" style="height:62px"></div></div>
      <div class="field" style="height:83px"><div class="field__label">Welcome message line</div><div class="field__input" style="height:30px;margin-top:16px"></div></div>
      <div class="field" style="height:104px"><div class="field__label">Rapid installer disclaimer</div><div class="field__input" style="height:64px"></div></div>
      <div class="field" style="height:100px"><div class="field__label">Pop up message 1</div><div class="field__input" style="height:62px"></div></div>
      <div class="field" style="height:102px"><div class="field__label">Video Playlist names</div><div class="field__input" style="height:62px"></div></div>
    </div>
  </div>
  <footer class="footer">Copyrights© 2018 . All Rights Reserved.</footer>
</section>

</body>
</html>
```